Brochure Design Project for a Psychotherapy Private Practice.

I am a psychologist and I own my private practice. I need brochures to market to doctors and healthcare providers so that they understand the psychotherapy services that I deliver. I also want the brochures to be informative to potential patients. I have included a word document that details the services that I offer.
Target Market(s)
Referring healthcare providers (medical doctors, naturopaths, physician assistants, nurse practitioners) and patients who are seeking psychotherapy.
Industry/Entity Type
Healthcare
Colors
Designer to choose colors to be used in the design.
Look and feel

```html
<!DOCTYPE html>
<html lang="en">
<head>
<meta charset="utf-8">
<title>Harbor Point Psychological Services – Trifold Brochure</title>
<link rel="stylesheet" href="https://fonts.googleapis.com/css2?family=Fira+Sans:wght@300;400;600&family=Source+Sans+3:wght@400;600&display=swap">
<style>
  :root {
    --page-bg: #fdf0cf;
    --teal-dark: #3f5f68;
    --teal-band: #4d6d76;
    --teal-text: #35575f;
    --ink: #1d1d1d;
    --paper: #ffffff;
    --grey-light: #f1f1f1;
    --grey-mid: #c9cacb;
    --grey-deep: #8f9294;
  }
  * { box-sizing: border-box; margin: 0; padding: 0; }
  html, body { width: 1200px; height: 1200px; overflow: hidden; background: var(--page-bg); }
  .canvas { position: relative; width: 1200px; height: 1200px; background: var(--page-bg); }

  .brochure {
    position: absolute; left: 46px; top: 301px; width: 1108px; height: 369px;
    display: flex; box-shadow: 3px 3px 4px rgba(0,0,0,0.18);
  }
  .panel { position: relative; width: 369.33px; height: 100%; overflow: hidden; }

  /* Left panel */
  .panel--steps { background: var(--grey-light); }
  .panel-art {
    position: absolute; inset: 0;
    background: linear-gradient(180deg, #eeeeee 0%, #f3f3f3 55%, #bdbebf 100%);
  }
  .panel-art--left::after {
    content: ""; position: absolute; left: 0; right: 0; top: 0; height: 45px;
    background: linear-gradient(90deg, rgba(70,75,78,0.35), rgba(70,75,78,0.05) 60%, rgba(70,75,78,0.3));
  }
  .section-tab {
    position: absolute; left: 0; top: 26px; width: 168px; height: 20px;
    background: var(--teal-band); border-radius: 0 10px 10px 0;
    color: var(--paper); font: 600 14px/20px "Fira Sans", sans-serif; padding-left: 32px;
  }
  .step-card {
    position: absolute; left: 20px; width: 317px; background: var(--paper);
    border-radius: 6px; box-shadow: 2px 2px 3px rgba(0,0,0,0.3);
    padding: 12px 14px 0 14px;
  }
  .step-card--consult { top: 55px; height: 114px; }
  .step-card--intake { top: 186px; height: 139px; }
  .step-title { font: 600 14.5px/1 "Fira Sans", sans-serif; color: var(--teal-text); margin-bottom: 6px; }
  .step-text { font: 400 9.6px/12.3px "Source Sans 3", sans-serif; color: var(--ink); }

  /* Middle panel */
  .panel--contact { background: var(--paper); }
  .bio-band {
    position: absolute; left: 0; right: 0; top: 49px; height: 126px; background: var(--teal-band);
  }
  .portrait {
    position: absolute; left: 34px; top: 12px; width: 72px; height: 72px; border-radius: 50%;
    border: 2px solid #e9e4df; background: radial-gradient(circle at 50% 45%, #c79a7e, #7a5343 70%);
  }
  .person-name {
    position: absolute; left: 20px; width: 100px; top: 88px; text-align: center;
    font: 600 9.4px/1.2 "Fira Sans", sans-serif; color: var(--paper);
  }
  .person-role { display: block; font-weight: 400; font-size: 7.8px; color: #dfe6e8; }
  .bio-text {
    position: absolute; left: 119px; top: 19px; width: 235px; text-align: justify;
    font: 400 7.5px/9.5px "Source Sans 3", sans-serif; color: #e8eef0;
  }
  .contact-list { position: absolute; left: 34px; top: 200px; }
  .contact-label { font: 600 12px/1 "Fira Sans", sans-serif; color: var(--teal-text); }
  .contact-value { font: 600 19px/1 "Fira Sans", sans-serif; color: var(--teal-text); margin-bottom: 9px; margin-top: 1px; }
  .address {
    position: absolute; left: 0; right: 0; top: 323px; text-align: center;
    font: 400 8px/10.5px "Source Sans 3", sans-serif; color: #444;
  }

  /* Right panel */
  .panel--cover { background: var(--grey-light); }
  .panel-art--cover {
    background:
      radial-gradient(ellipse 95px 120px at 130px 200px, #3d5962 0%, #56737c 60%, rgba(86,115,124,0) 100%),
      linear-gradient(180deg, #efefef 0%, #f4f4f4 60%, #c3c4c5 100%);
  }
  .tagline {
    position: absolute; left: 229px; top: 202px;
    font: 600 12.2px/15.8px "Fira Sans", sans-serif; color: var(--teal-text);
  }
  .brand-box {
    position: absolute; left: 212px; top: 266px; width: 158px; height: 61px;
    background: var(--paper); box-shadow: 0 2px 2px rgba(0,0,0,0.25);
  }
  .brand-dot {
    position: absolute; left: 23px; top: 17px; width: 26px; height: 26px; border-radius: 50%;
    background: var(--teal-dark);
  }
  .brand-name {
    position: absolute; left: 57px; top: 10px;
    font: 300 12px/13.5px "Fira Sans", sans-serif; color: var(--teal-dark);
  }
</style>
</head>
<body>
<main class="canvas">
  <article class="brochure">

    <section class="panel panel--steps">
      <div class="panel-art panel-art--left" role="img" aria-label="Grey backdrop with scattered 3D puzzle pieces"></div>
      <h2 class="section-tab">Getting Started:</h2>
      <div class="step-card step-card--consult">
        <h3 class="step-title">Consultation</h3>
        <p class="step-text">I offer a complimentary 30-minute consultation (on the phone), so you can get a sense of whether we are a good fit. It will also give me an opportunity to determine if I am the best therapist to be able to help you. In the event that we are not a good match, I can connect you with another practitioner to serve your needs.</p>
      </div>
      <div class="step-card step-card--intake">
        <h3 class="step-title">Intake</h3>
        <p class="step-text">During our first session, we will address your presenting problem(s) and collect a thorough background of your history, so that I can best understand your problem areas in the context of who you are. We will also conduct an assessment of your current symptoms, address provisional diagnoses (if applicable), discuss potential treatment goals, and develop a tentative treatment plan with recommendations for therapy duration and frequency.</p>
      </div>
    </section>

    <section class="panel panel--contact">
      <div class="bio-band">
        <div class="portrait" role="img" aria-label="Portrait photo of the psychologist"></div>
        <p class="person-name">Elena Marris<span class="person-role">Psychologist, PsyD</span></p>
        <p class="bio-text">Dr. Marris graduated from Westbrook University and received her Doctoral degree in Clinical Psychology at the Bayline School of Professional Psychology, Lakemont. She completed her predoctoral internship in behavioral medicine and rehabilitation psychology at the Northfield Veterans Healthcare System/Northfield Medical School and a postdoctoral fellowship at the Cognitive Intensive Outpatient Program, Crestview Hospital, Lakemont. Dr. Marris is a member of the National Psychological Society, Institute of Cognitive Practice, and the Coastal County Psychological Association.</p>
      </div>
      <div class="contact-list">
        <p class="contact-label">For Appointments</p>
        <p class="contact-value">000 000 0000</p>
        <p class="contact-label">Mail Us</p>
        <p class="contact-value">info@harborpointpsych.com</p>
        <p class="contact-label">Website</p>
        <p class="contact-value">www.harborpointpsych.com</p>
      </div>
      <p class="address">Address: Lorem ipsum dolor sit amet, consectetuer,<br>adipiscing elit, sed diam nonummy, euismod</p>
    </section>

    <section class="panel panel--cover">
      <div class="panel-art panel-art--cover" role="img" aria-label="Illustration of a human head made of teal puzzle pieces breaking apart"></div>
      <p class="tagline">a<br>practical<br>approach<br>to problem-solving</p>
      <div class="brand-box">
        <span class="brand-dot"></span>
        <p class="brand-name">Harbor Point<br>Psychological<br>Services</p>
      </div>
    </section>

  </article>
</main>
</body>
</html>
```